The Merry Hound - Dog Training Business Card Design

I need a business card design for a new dog training company based in Cronulla NSW called The Merry Hound. I run puppy pre school classes, adult dog classes and do one on one training in the person's home.
I have studied for 2 years and use positive reinforcement training methods based on how dogs learn. I believe in communicating with our dogs what we want them to do rather than punish them for behaviours we don't like. I would like to see designs that use the colours that are used in my logo (please see attached)
I would like a simple and classic looking design. I don't want cartoon images of dogs or any animal images or drawings on the card. I have created my logo with this mindset. I am open to the subtle use of a dog's tail, paws or paw print.

Target Market(s)

high end area which is why I want a classic looking design
adults aged 25 and over

Industry/Entity Type

Dog Training

Contact Information for Business Card

Miriam Caslett
ORBIS Trained Professional Dog Trainer
www.themerryhound-example.com.au
0499731628
miriam@themerryhound-example.com.au

Font styles to use
Sans Serif

Colors
ffffff
86cae6
757575

Requirements
Must have
• Logo - I am trying to attach my logo and colour palette but it won't allow me. I will contact the company and upload ASAP.
Should not have
• images of dogs or cartoon drawings

```html
<!DOCTYPE html>
<html lang="en">
<head>
<meta charset="utf-8">
<title>The Merry Hound – Business Card</title>
<link rel="stylesheet" href="https://fonts.googleapis.com/css2?family=Quicksand:wght@400;500&family=Open+Sans:wght@400;600&display=swap">
<style>
  :root {
    --white: #ffffff;
    --sky: #86cae6;
    --sky-pale: #dcebf4;
    --sky-mid: #b7d2e3;
    --grey: #757575;
    --grey-light: #a9a9a9;
    --name-blue: #7fa9c9;
    --stage: #eceae6;
  }
  * { box-sizing: border-box; margin: 0; padding: 0; }
  html, body { width: 1200px; height: 1023px; overflow: hidden; }
  body {
    background: var(--stage);
    font-family: "Open Sans", sans-serif;
    position: relative;
  }
  .card {
    position: absolute;
    top: 346px;
    width: 540px;
    height: 330px;
    border-radius: 4px;
    overflow: hidden;
    box-shadow: 0 4px 14px rgba(0,0,0,0.12);
  }
  .card--front {
    left: 40px;
    background: linear-gradient(160deg, var(--sky-pale) 0%, var(--sky-mid) 100%);
  }
  .card--back { left: 620px; background: var(--white); }

  .paw-heart {
    position: absolute;
    border-radius: 50% 50% 48% 48%;
    background: radial-gradient(circle at 50% 50%, rgba(255,255,255,0.75), rgba(255,255,255,0.15) 70%, rgba(255,255,255,0) 100%);
  }
  .card--front .paw-heart { left: 34px; top: 92px; width: 220px; height: 200px; }

  .brand { position: absolute; text-align: right; }
  .brand__name {
    font-family: "Quicksand", sans-serif;
    font-weight: 400;
    color: var(--grey);
    display: flex;
    align-items: center;
    gap: 10px;
    justify-content: flex-end;
    white-space: nowrap;
  }
  .brand__dot { width: 14px; height: 14px; border-radius: 50%; background: var(--white); flex: none; }
  .brand__tagline {
    font-family: "Quicksand", sans-serif;
    font-weight: 500;
    color: var(--white);
    letter-spacing: 0.2em;
    text-transform: uppercase;
  }
  .card--front .brand { right: 30px; top: 118px; }
  .card--front .brand__name { font-size: 40px; }
  .card--front .brand__tagline { font-size: 12px; margin-top: 6px; }

  .back-art { position: absolute; inset: 0; }
  .card--back .brand { left: 26px; top: 30px; text-align: left; }
  .card--back .brand__name { font-size: 30px; justify-content: flex-start; }
  .card--back .brand__tagline { font-size: 10px; margin-top: 5px; }
  .card--back .paw-heart { right: 26px; top: 16px; width: 110px; height: 100px; }

  .contact { position: absolute; left: 70px; top: 166px; color: var(--grey); }
  .contact__name { font-size: 17px; color: var(--name-blue); }
  .contact__title { font-size: 11.5px; margin: 3px 0 8px; }
  .contact__row { display: flex; align-items: center; gap: 7px; font-size: 11.5px; line-height: 19px; }
  .contact__row svg { width: 11px; height: 11px; flex: none; }

  .back-mark {
    position: absolute;
    right: 26px; bottom: 30px;
    font-family: "Quicksand", sans-serif;
    font-weight: 400;
    font-size: 20px;
    color: var(--grey-light);
  }
</style>
</head>
<body>

<section class="card card--front" aria-label="Card front">
  <div class="paw-heart" role="img" aria-label="Heart shape formed from small paw prints"></div>
  <div class="brand">
    <div class="brand__name"><span class="brand__dot"></span>The Merry Hound</div>
    <div class="brand__tagline">Positive Training Specialist</div>
  </div>
</section>

<section class="card card--back" aria-label="Card back">
  <svg class="back-art" viewBox="0 0 540 330" preserveAspectRatio="none" aria-hidden="true">
    <defs>
      <linearGradient id="band" x1="0" y1="0" x2="1" y2="1">
        <stop offset="0" stop-color="#dcebf4"/>
        <stop offset="1" stop-color="#b7d2e3"/>
      </linearGradient>
    </defs>
    <rect x="0" y="0" width="540" height="130" fill="url(#band)"/>
    <line x1="0" y1="130" x2="540" y2="130" stroke="#a9a9a9" stroke-width="3"/>
    <path d="M0 130 C 40 200, 20 280, 0 330 Z" fill="url(#band)"/>
    <path d="M0 330 C 60 300, 70 230, 40 130" fill="none" stroke="#a9a9a9" stroke-width="1.5"/>
  </svg>

  <div class="brand">
    <div class="brand__name"><span class="brand__dot"></span>The Merry Hound</div>
    <div class="brand__tagline">Positive Training Specialist</div>
  </div>
  <div class="paw-heart" role="img" aria-label="Small heart shape formed from paw prints"></div>

  <div class="contact">
    <p class="contact__name">Miriam Caslett ORBIS</p>
    <p class="contact__title">Trained Professional Dog Trainer</p>
    <p class="contact__row">
      <svg viewBox="0 0 12 12"><rect x="3" y="0.5" width="6" height="11" rx="1.2" fill="none" stroke="#757575"/><line x1="5" y1="9.5" x2="7" y2="9.5" stroke="#757575"/></svg>
      0499731628
    </p>
    <p class="contact__row">
      <svg viewBox="0 0 12 12"><rect x="0.5" y="2.5" width="11" height="7" fill="none" stroke="#757575"/><path d="M0.5 2.5 L6 7 L11.5 2.5" fill="none" stroke="#757575"/></svg>
      miriam@themerryhound-example.com.au
    </p>
    <p class="contact__row">
      <svg viewBox="0 0 12 12"><circle cx="6" cy="6" r="5.5" fill="none" stroke="#757575"/><ellipse cx="6" cy="6" rx="2.4" ry="5.5" fill="none" stroke="#757575"/><line x1="0.5" y1="6" x2="11.5" y2="6" stroke="#757575"/></svg>
      www.themerryhound-example.com.au
    </p>
  </div>

  <div class="back-mark">The Merry Hound</div>
</section>

</body>
</html>
```